Flyer Design / Authenticity Certificate - Art Work

Looking for a design of a "Authenticity Certificate" - flyer, that will include some basic company info like logo etc, and allow our in house artist to sign and authenticate before it is applied the reverse of one of the paintings we will sell. Linked with our online sales website - "Copper Hollow Canvases", where we recreate one off oil paintings from digital photographs. Our business logo should be incorporated in the design, along with a section for "Artisit Name" "Artisit Signature" "Ref Code"
Updates

Hi.. Sorry I should have added the size we need - please design accordingly to A6. Thanks.

Industry/Entity Type

It Company

Font styles to use
Serif
Script

Colors

Designer to choose colors to be used in the design.

Requirements
Must have
• Company logo
• Area for artist to print and sign
• Area for a reference
Nice to have
• must use the logo, maybe incorporate a "seal" icon, like what was used as a wax seal on older style documents

```html
<!DOCTYPE html>
<html lang="en">
<head>
<meta charset="utf-8">
<title>Certificate of Authenticity – Copper Hollow Canvases</title>
<link href="https://fonts.googleapis.com/css2?family=Cinzel:wght@400;500&family=Great+Vibes&family=Lato:wght@400;700&display=swap" rel="stylesheet">
<style>
  :root {
    --charcoal: #5f6062;
    --ink: #3a3a3c;
    --text: #1f1f21;
    --brand-silver: #cfd0d2;
    --orange: #f07a24;
    --orange-deep: #d4531c;
    --crimson: #e01e44;
    --sky: #28a8e0;
    --rule: #a01c2c;
    --paper-top: #ffffff;
    --paper-bottom: #e3e4e6;
    --gold-light: #f6d77a;
    --gold: #d9a431;
    --gold-deep: #9a6a14;
  }
  * { margin: 0; padding: 0; box-sizing: border-box; }
  html, body { width: 1200px; height: 851px; overflow: hidden; background: #ffffff; }
  .certificate {
    position: relative;
    width: 1200px;
    height: 851px;
    overflow: hidden;
    background: linear-gradient(180deg, var(--paper-top) 35%, var(--paper-bottom) 100%);
    font-family: "Lato", sans-serif;
    color: var(--text);
  }
  .header-band {
    position: absolute;
    left: 0; top: 0;
    width: 1200px; height: 120px;
    background: var(--charcoal);
  }
  .header-decoration {
    position: absolute;
    left: 0; top: 120px;
    width: 1200px; height: 140px;
    background:
      linear-gradient(180deg, rgba(255,255,255,0) 0%, rgba(255,255,255,0) 45%, var(--paper-top) 100%),
      linear-gradient(100deg, var(--orange) 0%, var(--orange-deep) 35%, var(--crimson) 65%, var(--sky) 100%);
  }
  .brand-name {
    position: absolute;
    right: 60px;
    top: 38px;
    font-family: "Lato", sans-serif;
    font-weight: 700;
    font-size: 36px;
    letter-spacing: 3px;
    text-transform: uppercase;
    color: var(--brand-silver);
    white-space: nowrap;
  }
  .heading {
    position: absolute;
    left: 480px;
    width: 670px;
    text-align: center;
    font-family: "Cinzel", serif;
    color: var(--ink);
  }
  .heading-main { top: 296px; font-size: 86px; font-weight: 400; letter-spacing: 3px; line-height: 1; }
  .heading-sub { top: 386px; font-size: 42px; font-weight: 400; letter-spacing: 2px; line-height: 1; }
  .statement {
    position: absolute;
    left: 480px; width: 670px; top: 452px;
    text-align: center;
    font-size: 19px;
    text-transform: uppercase;
  }
  .artist-name {
    position: absolute;
    left: 470px; width: 700px; top: 480px;
    text-align: center;
    font-family: "Great Vibes", cursive;
    font-size: 150px;
    line-height: 1.1;
    color: var(--ink);
    white-space: nowrap;
  }
  .signature-line {
    position: absolute;
    left: 482px; top: 749px;
    width: 304px; height: 3px;
    background: var(--rule);
  }
  .signature-label {
    position: absolute;
    left: 482px; width: 304px; top: 758px;
    text-align: center;
    font-size: 19px;
    text-transform: uppercase;
  }
  .reference {
    position: absolute;
    left: 894px; width: 240px; top: 740px;
    text-align: center;
    font-size: 20px;
    line-height: 26px;
  }
  .reference-label { text-transform: uppercase; }
  .seal {
    position: absolute;
    left: 62px; top: 440px;
    width: 358px; height: 358px;
    border-radius: 50%;
    background: radial-gradient(circle at 40% 35%, var(--gold-light) 0%, var(--gold) 45%, var(--gold-deep) 100%);
    box-shadow: 0 14px 24px rgba(0,0,0,0.22);
  }
</style>
</head>
<body>
  <main class="certificate">
    <div class="header-band"></div>
    <div class="header-decoration" role="img" aria-label="Flowing orange, red and blue ribbon decoration"></div>

    <div class="brand-name">Copper Hollow Canvases</div>

    <h1 class="heading heading-main">CERTIFICATE</h1>
    <h2 class="heading heading-sub">Of Authenticity</h2>
    <p class="statement">This is to certify that this artwork is authentic</p>

    <div class="artist-name">Artist Name</div>

    <div class="signature-line"></div>
    <div class="signature-label">Artist Signature</div>

    <div class="reference">
      <div class="reference-label">Reference Code:</div>
      <div class="reference-value">ABC-1234-XXX</div>
    </div>

    <div class="seal" role="img" aria-label="Gold wax seal of authenticity"></div>
  </main>
</body>
</html>
```